Create a landing page for my local business that I’m looking to advertise

I own an oriental rug repair, restoration and cleaning business.
I’m looking to rug advertising and i would like a very clear *******UX and UI design******* website designed.

pages that i need:
-Repair and restoration
-Cleaning
-Blocking
-Staircase rug installation
_about us
-homepage
-our story
-contact us
-estimate

Www.velborugs.example

Industry/Entity Type

Rug Industry, Antique and New Rug Repair restoration and cleaning

Number of Pages Required

5+ page

Font styles to use
Serif
Sans Serif
Script

Colors
6B429C
8869AF
B7A5CE
E3DAEB
F3F0F8

Requirements
Must have
• IT HAS TO PRESENT FINE RUG REPAIR, RESTORATION AND CLEANING.
Should not have
• I DONT WANT THE WEBSITE TO LOOK LIKE A GENERIC “CLEANING COMPANY”. WE ARE A HIGH END RUG REPAIR ,RESTORATION AND CLEANING COMPANY

```html
<!DOCTYPE html>
<html lang="en">
<head>
<meta charset="utf-8">
<title>Velbo Rugs — Oriental Rug Repair</title>
<link href="https://fonts.googleapis.com/css2?family=Bodoni+Moda:wght@400;500&family=PT+Sans:wght@400;700&family=Roboto+Condensed:wght@400;500&family=Roboto:wght@400;500&display=swap" rel="stylesheet">
<style>
:root{
  --accent:#6b429c;
  --accent-mid:#8869af;
  --accent-soft:#b7a5ce;
  --accent-pale:#e3daeb;
  --accent-mist:#f3f0f8;
  --black:#000;
  --ink:#222;
  --text:#555;
  --white:#fff;
  --overlay:rgba(60,48,78,.72);
}
*{margin:0;padding:0;box-sizing:border-box}
html,body{width:1200px;height:2866px;overflow:hidden;background:var(--white)}
body{position:relative;font-family:"PT Sans",sans-serif;color:var(--text)}
.abs{position:absolute}
.serif{font-family:"Bodoni Moda",serif;font-weight:400;text-transform:uppercase}
.btn{position:absolute;display:flex;align-items:center;justify-content:center;border-radius:24px;font-family:"Roboto Condensed",sans-serif;font-weight:500;font-size:15px;text-transform:uppercase;box-shadow:0 4px 8px rgba(0,0,0,.18)}
.btn-accent{background:var(--accent);color:var(--white)}
.btn-white{background:var(--white);color:var(--accent)}
.btn-static{position:relative;display:inline-flex}

/* header */
.site-header{left:0;top:0;width:1200px;height:128px;background:var(--black)}
.brand{left:111px;top:30px;color:var(--accent-soft)}
.brand-name{font-family:"Bodoni Moda",serif;font-size:44px;line-height:46px;letter-spacing:1px;font-weight:400}
.brand-tag{font-family:"Bodoni Moda",serif;font-size:10px;letter-spacing:3.6px;margin-top:6px}
.social-dot{top:18px;width:28px;height:28px;border-radius:50%;background:#555}
.lang{left:668px;top:24px;color:var(--white);font-family:"Roboto",sans-serif;font-size:14px;font-weight:500}
.flag{left:713px;top:18px;width:28px;height:28px;border-radius:50%;background:linear-gradient(#c8102e 0 15%,#fff 15% 30%,#c8102e 30% 45%,#fff 45% 60%,#c8102e 60% 75%,#fff 75% 90%,#c8102e 90%)}
.call{left:772px;top:16px;display:flex;align-items:center;gap:10px;color:var(--white);font-family:"Roboto",sans-serif}
.call small{font-size:15px;font-weight:500}
.call b{font-size:21px;font-weight:500}
.main-nav{right:113px;top:79px;display:flex;gap:35px;color:var(--white);font-family:"Roboto Condensed",sans-serif;font-weight:500;font-size:16px;text-transform:uppercase}

/* hero */
.hero{left:0;top:128px;width:1200px;height:686px;background:linear-gradient(110deg,#9c9a96 0%,#c9c6c1 40%,#b4aca3 70%,#8f877f 100%)}
.hero-panel{left:0;top:254px;width:574px;height:264px;background:var(--overlay)}
.hero-title{left:110px;top:278px;color:var(--white);font-size:52px;line-height:52px;white-space:nowrap}
.hero-sub{left:110px;top:394px;color:var(--white);font-size:22px}
.slide-arrow{left:1121px;width:45px;height:45px;border-radius:50%;background:rgba(40,40,40,.75);display:flex;align-items:center;justify-content:center}

/* services */
.service{top:604px;width:326px;height:363px;box-shadow:0 14px 22px rgba(0,0,0,.12)}
.service-photo{height:210px}
.service-body{position:relative;height:153px;background:var(--accent);text-align:center;padding-top:24px}
.service-body h3{font-family:"Roboto Condensed",sans-serif;font-weight:500;font-size:22px;color:var(--white);text-transform:uppercase}
.service-body .btn{left:62px;top:66px;width:208px;height:48px}

/* about */
.about-frame{left:86px;top:1043px;width:467px;height:424px;border:9px solid var(--accent)}
.about-photo{left:111px;top:1071px;width:468px;height:424px;background:linear-gradient(160deg,#4d5450,#5b4a38 60%,#3f3c36)}
.about-copy{left:622px;top:1064px;width:470px}
.about-title{color:var(--ink);font-size:36px;line-height:43px;white-space:nowrap;margin-bottom:20px}
.about-text{font-size:13.3px;line-height:21.5px;color:#666}
.about-text p+p{margin-top:21px}
.about-copy .btn{margin-top:25px;width:208px;height:48px}

/* original */
.orig-band{left:0;top:1598px;width:600px;height:522px;background:var(--accent)}
.orig-photo{left:600px;top:1598px;width:600px;height:522px;background:linear-gradient(170deg,#e3e0dc 0%,#cfc9c2 45%,#9a938c 70%,#c9a58a 100%)}
.orig-copy{left:106px;top:1686px;width:470px}
.orig-title{color:var(--white);font-size:36px;line-height:43px;white-space:nowrap;margin-bottom:16px}
.orig-text{color:var(--white);font-size:13.3px;line-height:21.5px}
.orig-copy .btn{margin-top:25px;width:208px;height:48px}

/* cta */
.cta-title{left:0;top:2214px;width:1200px;text-align:center;color:var(--ink);font-size:36px;line-height:43px}

/* footer */
.site-footer{left:0;top:2470px;width:1200px;height:396px;background:var(--black);font-family:"Roboto",sans-serif}
.foot-brand{left:124px;top:2594px;color:var(--accent-soft);text-align:center;width:248px}
.foot-brand .brand-name{font-size:34px;line-height:36px}
.foot-brand .brand-tag{font-size:8px;letter-spacing:2.6px;margin-top:5px}
.foot-social{top:2655px;width:33px;height:33px;border:2px solid var(--white);border-radius:50%}
.foot-col h4{font-family:"Roboto",sans-serif;font-weight:500;font-size:21px;color:var(--white);margin-bottom:22px}
.quick li{list-style:none;color:var(--white);font-size:15px;line-height:34.5px}
.quick li::before{content:"»";margin-right:9px}
.contact-row{display:flex;gap:14px;color:var(--white);font-size:15px;line-height:22px;margin-bottom:22px}
.contact-row svg{flex:none;margin-top:4px}
.hours{color:var(--accent-soft);font-size:15px;line-height:22px}
.foot-rule{left:111px;top:2786px;width:978px;height:1px;background:#2a2a2a}
.copyright{left:0;top:2808px;width:1200px;text-align:center;color:var(--white);font-size:14px}
</style>
</head>
<body>

<header class="abs site-header"></header>
<div class="abs brand">
  <div class="brand-name">VELBO RUGS</div>
  <div class="brand-tag">REPAIR | RESTORATION | CLEANING</div>
</div>
<span class="abs social-dot" style="left:540px"></span>
<span class="abs social-dot" style="left:574px"></span>
<span class="abs social-dot" style="left:609px"></span>
<div class="abs lang">Eng ⌄</div>
<span class="abs flag"></span>
<div class="abs call">
  <svg width="34" height="34" viewBox="0 0 34 34"><circle cx="17" cy="17" r="15.5" fill="none" stroke="#b7a5ce" stroke-width="2"/><path d="M11 10l3-1 2 5-2 1.5c1 2.5 2.5 4 5 5l1.5-2 5 2-1 3c-7 0-13.5-6.5-13.5-13.5z" fill="#b7a5ce"/></svg>
  <span><small>Call us Today : </small><b>+1 555 010 4400</b></span>
</div>
<nav class="abs main-nav"><span>Repair and Restoration</span><span>Cleaning</span><span>Blocking Staircase Rug Installation</span></nav>

<section class="abs hero" role="img" aria-label="Bright bedroom with a large upholstered bed and a patterned rug"></section>
<div class="abs hero-panel"></div>
<h1 class="abs serif hero-title">Oriental Rug<br>Repair</h1>
<p class="abs hero-sub">Authenticity and perfection.</p>
<a class="btn btn-accent" style="left:111px;top:439px;width:208px;height:47px">Get a free estimate</a>
<div class="abs slide-arrow" style="top:358px"><svg width="14" height="9" viewBox="0 0 14 9"><path d="M1 8l6-6 6 6" fill="none" stroke="#fff" stroke-width="1.5"/></svg></div>
<div class="abs slide-arrow" style="top:409px"><svg width="14" height="9" viewBox="0 0 14 9"><path d="M1 1l6 6 6-6" fill="none" stroke="#fff" stroke-width="1.5"/></svg></div>

<div class="abs service" style="left:111px">
  <div class="service-photo" role="img" aria-label="Close-up of a colourful patchwork rug" style="background:linear-gradient(135deg,#6b4a3a,#c98a80 40%,#d9c49a 70%,#4a3a30)"></div>
  <div class="service-body"><h3>Antique Rug Repair</h3><a class="btn btn-white">Get a free estimate</a></div>
</div>
<div class="abs service" style="left:437px">
  <div class="service-photo" role="img" aria-label="White shag rug rolled on a wooden floor" style="background:linear-gradient(160deg,#e8e6e2,#cfcac3 50%,#7a5538)"></div>
  <div class="service-body"><h3>Sun Fade Damage</h3><a class="btn btn-white">Get a free estimate</a></div>
</div>
<div class="abs service" style="left:763px">
  <div class="service-photo" role="img" aria-label="Cleaning machine working on a patterned rug" style="background:linear-gradient(160deg,#a9b0b5,#8a9aa0 40%,#c9a7b0 75%,#b08aa0)"></div>
  <div class="service-body"><h3>Rug Stain Removal</h3><a class="btn btn-white">Get a free estimate</a></div>
</div>

<div class="abs about-frame"></div>
<div class="abs about-photo" role="img" aria-label="Vintage wooden cabinet with radio and plants against a grey wall"></div>
<div class="abs about-copy">
  <h2 class="serif about-title">We care and respect<br>the rugs we work on.</h2>
  <div class="about-text">
    <p>With over 30 years of expertise in restoring and cleaning precious rugs, we feel we have a duty to bring each rug to its former glory whenever this is possible. We are a family-owned and -operated area rug repair and restoration firm near Chicago, specializing in Oriental Rug Cleaning, Antique Rug Repair, Sun Fade Damage, Rug Stain Removal and many more services. We use the best cleaning solutions for our hand-wash services, as well as wool and silk rugs.</p>
    <p>We know the work and passion that was put into all handmade rugs; we appreciate the art and the traditions that go into making such beautiful pieces you bring into your home. Your appreciation for such loved and beautiful pieces is highly appreciated by us, and we respect your dedication to keeping your rugs in excellent condition. We want to contribute to this to the best of our abilities.</p>
  </div>
  <a class="btn btn-accent btn-static">Get a free estimate</a>
</div>

<div class="abs orig-band"></div>
<div class="abs orig-photo" role="img" aria-label="Living room with grey sectional sofa and patterned rug"></div>
<div class="abs orig-copy">
  <h2 class="serif orig-title">There is nothing<br>more precious than<br>the original.</h2>
  <p class="orig-text">We value authenticity and we built our name on restoring rugs by hand, bringing back to life and using pieces that are in your family for generations or that you invested in because you appreciate their craftsmanship. This is our contribution to keeping the authenticity in your homes, and teaching new generations about the value manual craftsmanship can build, to the state of calling it art.</p>
  <a class="btn btn-white btn-static">Get a free estimate</a>
</div>

<h2 class="abs serif cta-title">Antique Rug Repair | Oriental Rug<br>Restoration | Antique Rug Cleaning</h2>
<a class="btn btn-accent" style="left:496px;top:2318px;width:208px;height:48px">Get a free estimate</a>

<footer class="abs site-footer"></footer>
<div class="abs foot-brand">
  <div class="brand-name">VELBO RUGS</div>
  <div class="brand-tag">REPAIR | RESTORATION | CLEANING</div>
</div>
<span class="abs foot-social" style="left:162px"></span>
<span class="abs foot-social" style="left:205px"></span>
<span class="abs foot-social" style="left:248px"></span>
<span class="abs foot-social" style="left:290px"></span>

<div class="abs foot-col" style="left:442px;top:2548px">
  <h4>Quick Links</h4>
  <ul class="quick"><li>Home</li><li>About</li><li>Blog</li><li>Contact</li><li>Privacy policy</li></ul>
</div>
<div class="abs foot-col" style="left:664px;top:2548px">
  <h4>Contact us</h4>
  <div class="contact-row"><svg width="12" height="14" viewBox="0 0 12 14"><path d="M6 0a5 5 0 015 5c0 4-5 9-5 9S1 9 1 5a5 5 0 015-5z" fill="#b7a5ce"/><circle cx="6" cy="5" r="2" fill="#000"/></svg><span>418 Harrow Lane,<br>Elmbrook, IL 60099</span></div>
  <div class="contact-row"><svg width="12" height="12" viewBox="0 0 12 12"><path d="M1 1l3-1 2 3-1.5 1.5c.8 1.5 1.5 2.2 3 3L9 6l3 2-1 3C5 11 1 7 1 1z" fill="#b7a5ce"/></svg><span>(555) 014-2290</span></div>
  <div class="contact-row"><svg width="13" height="10" viewBox="0 0 13 10"><rect width="13" height="10" rx="1" fill="#b7a5ce"/><path d="M0 1l6.5 5L13 1" fill="none" stroke="#000" stroke-width="1.2"/></svg><span>info@velborugs.example</span></div>
</div>
<div class="abs foot-col" style="left:922px;top:2548px">
  <h4>Working hours</h4>
  <div style="display:flex;gap:12px">
    <svg width="13" height="13" viewBox="0 0 13 13" style="margin-top:4px"><circle cx="6.5" cy="6.5" r="5.5" fill="none" stroke="#b7a5ce" stroke-width="1.5"/><path d="M6.5 3.5v3h2.5" fill="none" stroke="#b7a5ce" stroke-width="1.5"/></svg>
    <div class="hours">Monday - Friday<br>10AM–5PM<br><br>Saturday 10AM–1PM<br>Sunday Closed</div>
  </div>
</div>
<div class="abs foot-rule"></div>
<p class="abs copyright">© Copyrights 2021 | Company name | All Rights Reserved</p>

</body>
</html>
```